長野県のお土産と言えば「信州そば」です。その数多くある商品の中から
ぱっと手に取っていただけるようなものにしていただきたい。
手書き文字で田舎感を出したい。
全体寸法:(ヨコ)150×(タテ)250+35×(マチ)50mm
(右貼りで底面は封筒と同じ形です。)
用紙:晒クラフト70g(沈んだ感じの印刷仕上がりになります。)
印刷:4色(カラー)印刷(特色でもOK)
裏面は一括表示・注意事項・簡単な食べ方を載せる予定です。(作成不要)
添付のEPSファイルはデザイン作成時に使用できるガイドです。
信州そばの写真画像は長野県のおみやげ物で、一番売れているそばです。
こちらに対抗できるデザインを希望しています!
カレーうどんの画像は袋の形状見本です。上部35mmは折り返します。

まずは、商品が陳列された時にぱっと目を引く緑色。
大きくはっきりとした「きつねそば」の文字。
右下のイラストも信州っぽさがあり、商品写真が仕上がりのイメージが出来る事。全体的にバランスが取れている。

初めて依頼をさせていただきましたので、どのようになるのかと不安でいっぱいでしたが、皆様方の高いレベルのご提案を沢山いただき、大変満足しております。
クライアント様のご要望を私共が引き出しきれていない部分もあり、制作しにくい事もあったかと思います。申し訳ありません。
良いご提案が沢山あり、選考には迷いました。実際時間もかかりました。
ご指名できなかった皆様方、これからもPlomvexを活用させて頂きたいと思いますので、今後ともよろしくお願い申し上げます。
ありがとうございます

```html
<!DOCTYPE html>
<html lang="ja">
<head>
<meta charset="utf-8">
<title>信州 きつねそば</title>
<link rel="stylesheet" href="https://fonts.googleapis.com/css2?family=Potta+One&display=swap">
<style>
  :root {
    --paper: #ffffff;
    --ink: #111111;
    --accent-red: #e0321e;
  }
  html, body {
    margin: 0;
    padding: 0;
    overflow: hidden;
    background: var(--paper);
  }
  .package-front {
    position: relative;
    width: 800px;
    height: 1200px;
    background: var(--paper);
    overflow: hidden;
    font-family: "Potta One", sans-serif;
    color: var(--ink);
  }
  .vertical {
    position: absolute;
    writing-mode: vertical-rl;
    text-orientation: upright;
    margin: 0;
    line-height: 1;
    font-weight: 400;
  }
  .region-stamp {
    left: 340px;
    top: 40px;
    padding: 10px 6px;
    font-size: 40px;
    border: 5px solid var(--ink);
    border-radius: 14px;
  }
  .tagline-noodle {
    left: 290px;
    top: 170px;
    font-size: 56px;
    letter-spacing: 1px;
  }
  .tagline-tofu {
    left: 222px;
    top: 200px;
    font-size: 56px;
    letter-spacing: 2px;
  }
  .product-name {
    left: 40px;
    top: 235px;
    font-size: 138px;
    letter-spacing: -22px;
  }
  .fox-illustration {
    position: absolute;
    left: 410px;
    top: 120px;
    width: 320px;
    height: 740px;
    background: linear-gradient(180deg, #f2f2f2 0%, #e2e2e2 100%);
    border-radius: 40% 40% 50% 50% / 20% 20% 40% 40%;
  }
  .buckwheat-seal {
    position: absolute;
    left: 285px;
    top: 900px;
  }
  .buckwheat-seal text {
    font-family: "Potta One", sans-serif;
    fill: var(--ink);
  }
  .net-weight {
    position: absolute;
    left: 572px;
    top: 985px;
    margin: 0;
    font-size: 24px;
    letter-spacing: 1px;
  }
</style>
</head>
<body>
  <main class="package-front">
    <p class="vertical region-stamp">信州</p>
    <p class="vertical tagline-noodle">生めんうまつゆ</p>
    <p class="vertical tagline-tofu">油揚げ?!</p>
    <h1 class="vertical product-name">「きつねそば」</h1>

    <div class="fox-illustration" role="img" aria-label="筆で描かれた黒い線のきつねの顔のイラスト、赤い頬"></div>

    <svg class="buckwheat-seal" width="200" height="140" viewBox="0 0 200 140" aria-label="そば粉100%使用">
      <ellipse cx="100" cy="70" rx="94" ry="64" fill="var(--accent-red)" stroke="var(--ink)" stroke-width="5"/>
      <text x="100" y="62" font-size="32" text-anchor="middle">そば粉</text>
      <text x="100" y="100" font-size="26" text-anchor="middle">100%使用</text>
    </svg>

    <p class="net-weight">130g×2袋入</p>
  </main>
</body>
</html>
```